Verpackungsdesign für Proteinpulver
Zielgruppe
Wir entwickeln und vermarkten Bio-Zertifizierte Nahrung/Nahrungsergänzungsmittel mit einem hohen Proteingehalt. Unsere Zielgruppe sind ernährungsbewusste Menschen die Wert auf eine hohe Qualität, Nachhaltigkeit und Natürlichkeit setzen und 25+ Jahre alt sind.
Aufgabenstellung
Das erste Produkt von TalMoorfink ist ein Bio-Wheyprotein-Pulver mit Bourbon-Vanille, das Design ist für das Label für die Verpackung bestimmt. Das Proteinpulver wird in Standbodenbeutel aus (braunem) Kraftpapier abgefüllt und soll mit Labeln auf der Vorder- und Rückseite beklebt werden. Die Label sind 150mm hoch und 110mm breit. Auf der Vorderseite soll der Markenname also 'TalMoorfink' stehen und der Name der Sorte. Da der genaue Name für die Sorte noch nicht fest steht kann für das Design erst einmal 'Bio-Vanille Whey' benutzt werden. Außerdem soll das EU-Biosiegel mit dem Text 'DE-ÖKO-047' und 'EU/Nicht-EU-Landwirtschaft' abgebildet sein und das Nettogewicht '600g'.
Das Label auf der Rückseite der Verpackung soll folgende Informationen enthalten:
*Nährwerte
*Zutaten
*Kreuzkontamination
*Verzehrempfehlung
*Barcode
Die Inhalte sind als Dateien angehängt.

```html
<!DOCTYPE html>
<html lang="de">
<head>
<meta charset="utf-8">
<title>TalMoorfink – Bio Vanille Whey Etikett, Farbvarianten</title>
<link rel="stylesheet" href="https://fonts.googleapis.com/css2?family=Archivo+Black&family=Oswald:wght@500;600&family=Roboto:wght@500&display=swap">
<style>
  :root {
    --page-bg: #ececec;
    --label-dark: #2f1a0c;
    --label-mid: #5a3412;
    --label-warm: #6e4216;
    --frame: #9a7646;
    --white: #ffffff;
    --ink-dark: #2a1a0c;
    --organic-green: #7fb729;
    --accent-sand: #f3cf8e;
    --accent-green: #8dbb2a;
    --accent-orange: #f0920f;
    --vanilla-light: #efe6c8;
    --vanilla-pod: #2b2230;
  }
  * { box-sizing: border-box; margin: 0; padding: 0; }
  html, body { width: 1200px; height: 3000px; overflow: hidden; }
  body { background: var(--page-bg); }

  .variant {
    position: relative;
    width: 1200px;
    height: 1000px;
    display: flex;
    align-items: center;
    justify-content: center;
  }
  .variant--sand   { --accent: var(--accent-sand); }
  .variant--green  { --accent: var(--accent-green); }
  .variant--orange { --accent: var(--accent-orange); }

  .label {
    position: relative;
    width: 480px;
    height: 655px;
    background:
      radial-gradient(ellipse at 75% 35%, var(--label-warm) 0%, var(--label-mid) 40%, var(--label-dark) 100%);
  }
  .label__frame {
    position: absolute;
    inset: 20px;
    border: 10px solid var(--frame);
    outline: 1px solid var(--frame);
    outline-offset: -5px;
  }
  .brand-tab {
    position: absolute;
    top: 0;
    left: 50%;
    width: 105px;
    height: 134px;
    transform: translateX(-50%);
  }
  .brand-tab svg { position: absolute; inset: 0; }
  .brand-tab__name {
    position: absolute;
    top: 50px;
    left: 0;
    width: 100%;
    text-align: center;
    font-family: "Oswald", sans-serif;
    font-weight: 600;
    font-size: 21px;
    line-height: 23px;
    letter-spacing: -0.3px;
    color: var(--ink-dark);
    text-transform: uppercase;
  }
  .product-title {
    position: absolute;
    top: 148px;
    left: 0;
    width: 100%;
    text-align: center;
    font-family: "Archivo Black", sans-serif;
    font-size: 70px;
    line-height: 64px;
    letter-spacing: -1px;
    text-transform: uppercase;
  }
  .product-title__flavour { display: block; color: var(--accent); }
  .product-title__type { display: block; color: var(--white); }

  .organic-seal {
    position: absolute;
    top: 365px;
    left: 65px;
    width: 70px;
    height: 46px;
    background: var(--organic-green);
  }
  .organic-seal__text {
    position: absolute;
    top: 416px;
    left: 50px;
    width: 100px;
    text-align: center;
    font-family: "Roboto", sans-serif;
    font-weight: 500;
    font-size: 8px;
    line-height: 11px;
    letter-spacing: 0.5px;
    color: var(--white);
  }
  .vanilla-visual {
    position: absolute;
    top: 380px;
    left: 60px;
    width: 365px;
    height: 200px;
    clip-path: polygon(0 78%, 55% 20%, 100% 10%, 100% 40%, 50% 100%, 5% 100%);
    background: linear-gradient(160deg, var(--vanilla-light) 0%, #b9a37a 35%, var(--vanilla-pod) 70%);
    opacity: 0.9;
  }
  .net-weight {
    position: absolute;
    top: 518px;
    left: 258px;
    font-family: "Oswald", sans-serif;
    font-weight: 500;
    font-size: 44px;
    line-height: 50px;
    color: var(--white);
    white-space: nowrap;
  }
  .net-weight__estimated { margin-left: 10px; font-family: "Roboto", sans-serif; font-weight: 500; }
</style>
</head>
<body>

  <section class="variant variant--sand">
    <article class="label">
      <div class="label__frame"></div>
      <div class="brand-tab">
        <svg viewBox="0 0 105 134" width="105" height="134"><polygon points="0,0 105,0 105,120 52.5,134 0,120" fill="var(--accent)"/></svg>
        <div class="brand-tab__name">Tal<br>Moorfink</div>
      </div>
      <h1 class="product-title"><span class="product-title__flavour">Bio<br>Vanille</span><span class="product-title__type">Whey</span></h1>
      <div class="organic-seal" role="img" aria-label="EU-Bio-Siegel"></div>
      <p class="organic-seal__text">DE-ÖKO-047<br>EU/Nicht-EU<br>Landwirtschaft</p>
      <div class="vanilla-visual" role="img" aria-label="Vanilleblüte mit Vanilleschoten"></div>
      <p class="net-weight">600 g<span class="net-weight__estimated">℮</span></p>
    </article>
  </section>

  <section class="variant variant--green">
    <article class="label">
      <div class="label__frame"></div>
      <div class="brand-tab">
        <svg viewBox="0 0 105 134" width="105" height="134"><polygon points="0,0 105,0 105,120 52.5,134 0,120" fill="var(--accent)"/></svg>
        <div class="brand-tab__name">Tal<br>Moorfink</div>
      </div>
      <h1 class="product-title"><span class="product-title__flavour">Bio<br>Vanille</span><span class="product-title__type">Whey</span></h1>
      <div class="organic-seal" role="img" aria-label="EU-Bio-Siegel"></div>
      <p class="organic-seal__text">DE-ÖKO-047<br>EU/Nicht-EU<br>Landwirtschaft</p>
      <div class="vanilla-visual" role="img" aria-label="Vanilleblüte mit Vanilleschoten"></div>
      <p class="net-weight">600 g<span class="net-weight__estimated">℮</span></p>
    </article>
  </section>

  <section class="variant variant--orange">
    <article class="label">
      <div class="label__frame"></div>
      <div class="brand-tab">
        <svg viewBox="0 0 105 134" width="105" height="134"><polygon points="0,0 105,0 105,120 52.5,134 0,120" fill="var(--accent)"/></svg>
        <div class="brand-tab__name">Tal<br>Moorfink</div>
      </div>
      <h1 class="product-title"><span class="product-title__flavour">Bio<br>Vanille</span><span class="product-title__type">Whey</span></h1>
      <div class="organic-seal" role="img" aria-label="EU-Bio-Siegel"></div>
      <p class="organic-seal__text">DE-ÖKO-047<br>EU/Nicht-EU<br>Landwirtschaft</p>
      <div class="vanilla-visual" role="img" aria-label="Vanilleblüte mit Vanilleschoten"></div>
      <p class="net-weight">600 g<span class="net-weight__estimated">℮</span></p>
    </article>
  </section>

</body>
</html>
```